Business Card Design

I would like a new business card design for an accounting firm that specializes in resolving clients tax problems. I want the card to give the impression that we are not your typical stodgy accounting firm, but at the same time we will get the job done.
Industry/Entity Type
Business
Contact Information for Business Card
Dorian T Welsby
Certified Public Accountant
38-27 52nd Street
Sunnyside, NY 11287
Tel: (718) 555-0142
Fax: (888) 555-0199
e-mail: dtwthecpa@ledgerpost.com
website: harborfilingreliefexperts.com

```html
<!DOCTYPE html>
<html lang="en">
<head>
<meta charset="utf-8">
<title>Dorian T. Welsby – Business Card</title>
<link rel="stylesheet" href="https://fonts.googleapis.com/css2?family=Playfair+Display:wght@700&family=Oswald:wght@500&family=Lato:wght@300;400;700&display=swap">
<style>
  :root {
    --stage: #636365;
    --navy: #033e7a;
    --gold: #f2b705;
    --paper: #e6e7e9;
    --white: #ffffff;
  }
  * { margin: 0; padding: 0; box-sizing: border-box; }
  html, body { width: 1200px; height: 1192px; overflow: hidden; background: var(--stage); }
  .card {
    position: absolute;
    left: 274px;
    width: 651px;
    height: 370px;
    border-radius: 22px;
  }
  .card--front { top: 157px; background: var(--navy); }
  .card--back { top: 634px; background: var(--paper); }

  .front__name {
    position: absolute;
    left: 0; right: 0; top: 138px;
    text-align: center;
    font-family: "Playfair Display", serif;
    font-weight: 700;
    font-size: 40px;
    letter-spacing: 3px;
    color: var(--white);
    line-height: 1;
  }
  .front__title {
    position: absolute;
    left: 0; right: 0; top: 186px;
    text-align: center;
    font-family: "Oswald", sans-serif;
    font-weight: 500;
    font-size: 25px;
    letter-spacing: 4.6px;
    color: var(--gold);
    line-height: 1;
  }

  .contact {
    position: absolute;
    right: 325px;
    text-align: right;
    font-family: "Lato", sans-serif;
    font-weight: 300;
    font-size: 19px;
    letter-spacing: 1px;
    color: var(--navy);
    line-height: 1;
    white-space: nowrap;
  }
  .icon {
    position: absolute;
    left: 341px;
    width: 18px;
    height: 18px;
    fill: var(--navy);
  }
  .signature {
    position: absolute;
    left: 418px;
    font-family: "Lato", sans-serif;
    color: var(--navy);
    line-height: 1;
    white-space: nowrap;
  }
  .signature__name { top: 280px; font-weight: 700; font-size: 19px; letter-spacing: -0.8px; }
  .signature__title { top: 304px; font-weight: 400; font-size: 16px; letter-spacing: -0.6px; }
</style>
</head>
<body>
  <section class="card card--front">
    <h1 class="front__name">DORIAN T. WELSBY</h1>
    <p class="front__title">CERTIFIED PUBLIC ACCOUNTANT</p>
  </section>

  <section class="card card--back">
    <p class="contact" style="top:154px">(718) 555-0142</p>
    <svg class="icon" style="top:153px" viewBox="0 0 20 20" aria-label="Telephone">
      <circle cx="10" cy="10" r="9" fill="none" stroke="#033e7a" stroke-width="1.6"/>
      <path d="M8 5h2l1 3-1.5 1c.5 1.2 1.3 2 2.5 2.5l1-1.5 3 1v2c-4 .5-8.5-3.5-8-8z" transform="translate(-1 0)"/>
    </svg>

    <p class="contact" style="top:182px">(888) 555-0199</p>
    <svg class="icon" style="top:181px" viewBox="0 0 20 20" aria-label="Fax">
      <circle cx="10" cy="10" r="9" fill="none" stroke="#033e7a" stroke-width="1.6"/>
      <rect x="7" y="4.5" width="6" height="4"/>
      <rect x="4.5" y="8" width="11" height="5" rx="1"/>
      <rect x="7" y="12" width="6" height="3.5" fill="#e6e7e9" stroke="#033e7a" stroke-width="1"/>
    </svg>

    <p class="contact" style="top:210px">dtwthecpa@ledgerpost.com</p>
    <svg class="icon" style="top:210px" viewBox="0 0 20 20" aria-label="Email">
      <rect x="1" y="4" width="18" height="12"/>
      <path d="M1 4l9 7 9-7M1 16l6.5-6M19 16l-6.5-6" fill="none" stroke="#e6e7e9" stroke-width="1.3"/>
    </svg>

    <p class="contact" style="top:237px">harborfilingreliefexperts.com</p>
    <svg class="icon" style="top:237px" viewBox="0 0 20 20" aria-label="Website">
      <circle cx="10" cy="10" r="8.5"/>
      <g fill="none" stroke="#e6e7e9" stroke-width="1.1">
        <ellipse cx="10" cy="10" rx="3.5" ry="8.5"/>
        <path d="M10 1.5v17M1.5 10h17M3 6h14M3 14h14"/>
      </g>
    </svg>

    <p class="contact" style="top:279px">38-27 52nd Street</p>
    <p class="contact" style="top:303px">Sunnyside, NY 11287</p>
    <svg class="icon" style="top:286px;width:20px;height:28px;left:339px" viewBox="0 0 20 28" aria-label="Address">
      <path d="M10 0C4.5 0 0.5 4 0.5 9.3 0.5 16 10 28 10 28s9.5-12 9.5-18.7C19.5 4 15.5 0 10 0z"/>
      <circle cx="10" cy="9.5" r="3.6" fill="#e6e7e9"/>
    </svg>

    <p class="signature signature__name">Dorian T Welsby</p>
    <p class="signature signature__title">Certified Public Accountant</p>
  </section>
</body>
</html>
```